Colm Vestry Personal Website Yoga Teacher and Personal Fitness Trainer

Let's pick a SITEFORGE theme that can work with Video Bckground. I would like a website design to look like some of nice Pagewright themes.
I would like to have a Video background of me teaching. I can provide video. Please view my current Siteforge site: www.colmvestry-example.com. I also have new logo. See file cves1.png

Project Deadline Extended
Reason: I am guaranteeing this project because i believe designers can deliver. I am extending 5 days because the homepage image/video slider is intricate and takes a bit of time. I have provided details, images, video etc. in Filecrate. Tx

Target Market(s)

All people needing & wanting personal help (they can trust and feel safe and nurtured) for their health (wellness, nutrition, fitness, exercise). And people wanting extraordinary yoga teaching.

Industry/Entity Type

Fitness

Number of Pages Required

5+ page

Colors
9bcb3b
add136
cadf82
eaf2ce

Requirements
Must have
• Template that can use a video background
Nice to have
• Need to show good image gallery and testimonial videos

```html
<!DOCTYPE html>
<html lang="en">
<head>
<meta charset="utf-8">
<title>Colm Vestry – Yoga Teacher and Personal Fitness Trainer</title>
<link href="https://fonts.googleapis.com/css2?family=Josefin+Sans:wght@400;600;700&family=Open+Sans:wght@400;600;700&display=swap" rel="stylesheet">
<style>
:root{
  --green:#9bcb3b;
  --green-deep:#add136;
  --green-soft:#cadf82;
  --green-pale:#eaf2ce;
  --gold:#b8962a;
  --blue:#1c1ccf;
  --ink:#333;
  --white:#fff;
  --footer:#777;
  --footer-dark:#4a4a4a;
  --paper:#f4f4f4;
}
*{margin:0;padding:0;box-sizing:border-box}
html,body{width:1200px;height:3734px;overflow:hidden}
body{font-family:"Open Sans",sans-serif;color:var(--ink);background:var(--white);position:relative}
section,header,footer{position:absolute;left:0;width:1200px}
.abs{position:absolute}
.heading{font-family:"Josefin Sans",sans-serif;font-weight:600;font-size:34px;color:#333;display:flex;align-items:center;gap:14px;justify-content:center}
.heading .rule{display:block;width:80px;height:3px;background:var(--blue);margin:6px auto 0}
.btn{display:inline-block;border:3px solid var(--white);color:var(--white);font-size:18px;padding:6px 24px;border-radius:3px;background:transparent}
.btn-blue{border-color:var(--blue);color:#222;background:var(--white)}

/* header */
.site-header{top:0;height:112px;background:var(--white)}
.brand{left:46px;top:12px;display:flex;align-items:center;gap:10px}
.brand-mark{width:44px;height:44px;border-radius:50%;background:var(--gold)}
.brand-name{font-size:25px;font-weight:600;color:var(--gold);letter-spacing:1px}
.brand-tag{left:46px;top:72px;font-size:10px;color:var(--gold)}
.phone{right:40px;top:14px;font-size:21px;color:#333;display:flex;align-items:center;gap:8px}
.nav{right:36px;top:60px;display:flex;gap:22px;font-size:17px;font-weight:600}
.nav a{color:#333;text-decoration:none;padding:4px 14px}
.nav a.current{border:2px solid var(--green);padding:2px 20px}

/* hero */
.hero{top:112px;height:493px;background:linear-gradient(120deg,#3c4a34,#5e6a4e 40%,#4a5540 70%,#2e3a2a)}
.hero-line{top:605px;height:5px;background:var(--blue)}

/* about */
.about{top:610px;height:380px;background:var(--paper)}
.about-text{left:68px;top:30px;width:530px}
.about-text h2{font-family:"Josefin Sans",sans-serif;font-size:32px;font-weight:600;display:flex;gap:14px;align-items:center;margin-bottom:12px}
.about-text p{font-size:18px;line-height:24px;margin-bottom:18px}
.about-photo{left:605px;top:0;width:595px;height:380px;background:linear-gradient(135deg,#e6ebe9,#cfd8d6 50%,#b9c6c2)}

/* gallery */
.gallery{top:990px;height:555px;background:#f7f7f7}
.gallery .heading{position:absolute;top:48px;width:100%}
.gallery .heading span{color:var(--green)}
.circle{position:absolute;border-radius:50%}
.gallery .circle{width:316px;height:316px;top:132px}
.gallery .btn-blue{position:absolute;left:537px;top:485px;font-size:17px;padding:4px 36px}

/* philosophy */
.philosophy{top:1545px;height:270px;background:linear-gradient(100deg,#6f9a2c,#a6c83a 50%,#8fb332 80%,#6f9a2c)}
.phil-list{right:930px;top:38px;text-align:right;color:var(--white);font-weight:700;font-size:18px;line-height:42px}
.phil-divider{left:312px;top:45px;height:180px;border-left:3px dotted var(--white)}
.phil-body{left:350px;top:38px;width:820px;color:var(--white)}
.phil-body h2{font-family:"Josefin Sans",sans-serif;font-weight:600;font-size:34px;margin-bottom:8px}
.phil-body p{font-size:16px;line-height:24px;margin-bottom:16px;color:#f2f7df}
.section-line{top:1815px;height:4px;background:var(--blue)}

/* services */
.services{top:1819px;height:701px;background:var(--green-soft)}
.services .heading{position:absolute;top:40px;width:100%}
.services .circle{width:230px;height:230px;top:110px}
.service{position:absolute;top:372px;width:330px;height:300px;text-align:center}
.service h3{font-size:23px;font-weight:700;color:var(--white);line-height:28px;height:56px;display:flex;align-items:flex-end;justify-content:center;margin-bottom:8px}
.service p{font-size:17px;line-height:24px;color:#222;height:120px;overflow:hidden}
.service .btn{position:absolute;left:92px;top:220px;font-size:17px;padding:4px 26px}

/* blog */
.blog{top:2520px;height:430px;background:linear-gradient(100deg,#6f9a2c,#a9ca3c 45%,#93b634 75%,#6f9a2c)}
.blog .heading{position:absolute;top:20px;width:100%;color:var(--white)}
.post{position:absolute;top:112px;width:330px;color:var(--white)}
.post-date{position:absolute;left:0;top:0;width:88px;height:104px;background:var(--green-pale);border-top:18px solid var(--blue);text-align:center;color:var(--white);font-weight:700;font-size:30px;line-height:32px;padding-top:10px;text-shadow:0 0 3px #7a9a3a}
.post h3{margin-left:100px;font-size:20px;line-height:26px;font-weight:700;height:80px}
.post .byline{margin-left:100px;font-size:14px}
.post p{position:absolute;top:130px;font-size:16px;line-height:24px}
.post .btn{position:absolute;top:246px;font-size:16px;padding:2px 24px}

/* testimonials */
.testimonials{top:2950px;height:360px;background:#f6f6f6}
.testimonials .heading{position:absolute;top:30px;width:100%}
.video{position:absolute;top:118px;width:330px;height:185px;box-shadow:0 10px 14px rgba(0,0,0,.25)}
.video-bar{position:absolute;left:0;bottom:0;width:100%;height:26px;background:rgba(30,30,30,.75)}
.video-bar i{position:absolute;left:44px;top:11px;width:220px;height:4px;background:#888}
.video-bar b{position:absolute;left:12px;top:7px;width:0;height:0;border-left:11px solid #ddd;border-top:6px solid transparent;border-bottom:6px solid transparent}
.footer-line{top:3310px;height:5px;background:var(--green)}

/* footer */
.site-footer{top:3315px;height:419px;background:var(--footer)}
.touch{top:18px;width:100%;text-align:center;font-size:32px;color:var(--blue)}
.social{top:78px;width:100%;display:flex;justify-content:center;gap:14px}
.social span{width:32px;height:32px;border:2px solid var(--white);border-radius:50%}
.fcol{position:absolute;top:136px;color:var(--white);font-size:14px;line-height:28px}
.fcol h4{color:var(--blue);font-size:21px;font-weight:600;margin-bottom:10px;line-height:24px}
.fcol ul{list-style:none;font-weight:700;font-size:13px;line-height:33px}
.fcol ul li::before{content:"›";color:var(--blue);margin-right:14px;font-size:16px}
.contact-row{display:flex;gap:10px;align-items:flex-start;line-height:33px}
.map{left:892px;top:176px;width:268px;height:125px;background:linear-gradient(135deg,#e6e8df,#d3d8c8 60%,#c6ccba)}
.copyright{position:absolute;left:0;top:375px;width:100%;height:44px;background:var(--footer-dark);color:var(--white);font-size:13px;text-align:center;line-height:44px}
</style>
</head>
<body>

<header class="site-header">
  <div class="abs brand"><span class="brand-mark"></span><span class="brand-name">COLM VESTRY</span></div>
  <div class="abs brand-tag">Personal Training • Diet &amp; Nutrition • Yoga &amp; Meditation</div>
  <div class="abs phone">
    <svg width="24" height="24" viewBox="0 0 24 24"><circle cx="12" cy="12" r="12" fill="#9bcb3b"/><path d="M8 6l2 3-1.3 1.3a8 8 0 0 0 5 5L15 14l3 2-1.2 2.2C11 18 6 13 5.8 7.2z" fill="#fff"/></svg>
    Call us now! 800-555-0147
  </div>
  <nav class="abs nav">
    <a class="current">HOME</a><a>ABOUT US</a><a>SERVICES</a><a>BLOG</a><a>GALLERY</a><a>CONTACT</a>
  </nav>
</header>

<section class="hero" role="img" aria-label="Video background: group yoga class smiling together outdoors">
  <svg class="abs" style="left:540px;top:190px" width="120" height="120" viewBox="0 0 120 120">
    <circle cx="60" cy="60" r="55" fill="none" stroke="rgba(255,255,255,.7)" stroke-width="7"/>
    <path d="M47 36 L86 60 L47 84Z" fill="rgba(255,255,255,.7)"/>
  </svg>
</section>
<div class="abs hero-line" style="left:0;width:1200px"></div>

<section class="about">
  <div class="abs about-text">
    <h2><svg width="36" height="36" viewBox="0 0 36 36"><circle cx="18" cy="18" r="18" fill="#1c1ccf"/><rect x="16" y="15" width="4" height="13" fill="#fff"/><circle cx="18" cy="10" r="2.5" fill="#fff"/></svg>About Us</h2>
    <p>This is the studio's version of Lorem Ipsum. Proin gravida nibh vel velit auctor aliquet. Aenean sollicitudin, lorem quis bibendum auctor, nisi elit consequat ipsum, nec sagittis sem nibh id elit. Duis sed odio sit amet nibh vulputate cursus a sit amet mauris. Morbi accumsan ipsum velit. Nam nec tellus a odio tincidunt auctor a ornare odio. Sed non mauris vitae erat consequat auctor eu in elit.</p>
    <span class="btn btn-blue">Read More</span>
  </div>
  <div class="abs about-photo" role="img" aria-label="Photo: group seated in meditation pose in a bright studio"></div>
</section>

<section class="gallery">
  <h2 class="heading">
    <svg width="34" height="28" viewBox="0 0 34 28"><rect x="2" y="2" width="30" height="24" fill="none" stroke="#1c1ccf" stroke-width="3"/><path d="M6 22l8-9 6 6 4-4 6 7z" fill="#1c1ccf"/><circle cx="24" cy="9" r="3" fill="#1c1ccf"/></svg>
    <span>Our Gallery<i class="rule"></i></span>
  </h2>
  <div class="circle" style="left:87px;background:radial-gradient(circle,#c84a3a,#4a7a3a 60%,#2f5a2a)" role="img" aria-label="Gallery photo: yoga teacher seated in lotus pose in a garden"></div>
  <div class="circle" style="left:442px;background:radial-gradient(circle,#e8e2d8,#8a8a7a 70%,#5a5a4a)" role="img" aria-label="Gallery photo: teacher in white seated with hands in prayer"></div>
  <div class="circle" style="left:802px;background:radial-gradient(circle,#d68a6a,#a85a4a 60%,#6a3a3a)" role="img" aria-label="Gallery photo: yoga stretch in a decorated studio"></div>
  <span class="btn btn-blue">All View</span>
</section>

<section class="philosophy">
  <div class="abs phil-list">philosophy<br>practice<br>life style<br>meditation</div>
  <div class="abs phil-divider"></div>
  <div class="abs phil-body">
    <h2>Philosophy</h2>
    <p>This is the studio's version of Lorem Ipsum. Proin gravida nibh vel velit auctor aliquet. Aenean sollicitudin, lorem quis bibendum auctor, nisi elit consequat ipsum, nec sagittis sem nibh id elit. Duis sed odio sit amet nibh vulputate cursus a sit amet mauris. Morbi accumsan ipsum velit. Nam nec tellus a odio tincidunt auctor a ornare odio.</p>
    <span class="btn">Read More</span>
  </div>
</section>
<div class="abs section-line" style="left:0;width:1200px"></div>

<section class="services">
  <h2 class="heading">
    <svg width="30" height="30" viewBox="0 0 30 30"><circle cx="15" cy="15" r="10" fill="none" stroke="#1c1ccf" stroke-width="6" stroke-dasharray="4 3"/><circle cx="15" cy="15" r="7" fill="#1c1ccf"/><circle cx="15" cy="15" r="3" fill="#cadf82"/></svg>
    <span>Our Services<i class="rule"></i></span>
  </h2>
  <div class="circle" style="left:130px;background:radial-gradient(circle,#e07a3a,#b85a2a 60%,#8a4a2a)" role="img" aria-label="Photo: person wrapped in orange shawl meditating"></div>
  <div class="circle" style="left:485px;background:radial-gradient(circle,#6aa84a,#c83a3a 50%,#3a3a6a)" role="img" aria-label="Photo: bowl of fresh fruit and vegetables"></div>
  <div class="circle" style="left:845px;background:radial-gradient(circle,#d88a6a,#a85a4a 60%,#5a3a2a)" role="img" aria-label="Photo: yoga teacher training assist"></div>
  <div class="service" style="left:80px"><h3>WORKSHOPS</h3><p>Change your brain for the better with meditation! A regular meditation practice leads to many benefits for the brain and increases an individual's sense of well-being.</p><span class="btn">Read More</span></div>
  <div class="service" style="left:435px"><h3>More on DIET &amp;<br>NUTRITION</h3><p>An old proverb: "Let food be thy medicine" Don't be yet another sad statistic of failing health due to overeating and poor nutrition choices. BE TRULY WELL and transform your</p><span class="btn">Read More</span></div>
  <div class="service" style="left:795px"><h3>COLM'S YOGA TEACHER'S<br>TRAINING</h3><p>From Colm: "Dear Friends of Yoga, I am so excited to lead the SPRING 2014 South Harbor 200-hour Professional Yoga Teacher Training Program at Quiet Lotus.</p><span class="btn">Read More</span></div>
</section>

<section class="blog">
  <h2 class="heading">
    <svg width="30" height="30" viewBox="0 0 30 30"><rect width="30" height="30" rx="4" fill="#1c1ccf"/><path d="M8 22l2-6 9-9 4 4-9 9z" fill="#fff"/></svg>
    <span>Latest From The Blog<i class="rule" style="background:var(--white)"></i></span>
  </h2>
  <article class="post" style="left:62px">
    <div class="post-date">22<br>Dec</div>
    <h3>Center your body and mind, Stretch the possibilities.</h3>
    <div class="byline">by Dana Ferrow</div>
    <p>Fusce euismod consequat ante. Lorem ipsum dolor sit amet, consectetuer adipiscing elit. Pellentesque sed dolor. Aliquam congue fermentum nisl.</p>
    <span class="btn">Read More</span>
  </article>
  <article class="post" style="left:447px">
    <div class="post-date">22<br>Dec</div>
    <h3>Yoga: It's a mind, body, spirit</h3>
    <div class="byline">by Dana Ferrow</div>
    <p>Fusce euismod consequat ante. Lorem ipsum dolor sit amet, consectetuer adipiscing elit. Pellentesque sed dolor. Aliquam congue fermentum nisl.</p>
    <span class="btn">Read More</span>
  </article>
  <article class="post" style="left:830px">
    <div class="post-date">22<br>Dec</div>
    <h3>Yoga Keeps the Body Healthy and the Mind Clear</h3>
    <div class="byline">by Dana Ferrow</div>
    <p>Fusce euismod consequat ante. Lorem ipsum dolor sit amet, consectetuer adipiscing elit. Pellentesque sed dolor. Aliquam congue fermentum nisl.</p>
    <span class="btn">Read More</span>
  </article>
</section>

<section class="testimonials">
  <h2 class="heading">
    <svg width="32" height="28" viewBox="0 0 32 28"><ellipse cx="13" cy="11" rx="12" ry="9" fill="#9bcb3b"/><ellipse cx="21" cy="17" rx="10" ry="8" fill="#7fa82e"/></svg>
    <span>Testimonial<i class="rule" style="background:var(--green)"></i></span>
  </h2>
  <div class="video" style="left:45px;background:linear-gradient(120deg,#c9c4bc,#8a7a6a 60%,#5a5048)" role="img" aria-label="Testimonial video: client speaking in an office"><div class="video-bar"><b></b><i></i></div></div>
  <div class="video" style="left:425px;background:linear-gradient(120deg,#d8dde2,#9aa6b0 60%,#4a5a6a)" role="img" aria-label="Testimonial video: client speaking outdoors"><div class="video-bar"><b></b><i></i></div></div>
  <div class="video" style="left:815px;background:linear-gradient(120deg,#e8e4e0,#c8b8a8 60%,#8a6a5a)" role="img" aria-label="Testimonial video: client speaking in a studio"><div class="video-bar"><b></b><i></i></div></div>
</section>
<div class="abs footer-line" style="left:0;width:1200px"></div>

<footer class="site-footer">
  <div class="abs touch">GET IN TOUCH</div>
  <div class="abs social"><span></span><span></span><span></span><span></span></div>
  <div class="fcol" style="left:50px;width:300px">
    <h4>ABOUT US</h4>
    <p style="font-size:13px;line-height:28px">This is the studio's version of Lorem Ipsum. Proin gravida nibh vel velit auctor aliquet. Aenean sollicitudin, lorem quis bibendum auctor, nisi elit consequat ipsum, nec sagittis sem nibh id elit. Duis sed odio sit amet nibh...</p>
  </div>
  <div class="fcol" style="left:405px">
    <h4>NAVIGATION</h4>
    <ul><li>HOME</li><li>ABOUT US</li><li>SERVICES</li><li>BLOG</li><li>GALLERY</li></ul>
  </div>
  <div class="fcol" style="left:597px;width:280px;font-size:13px">
    <h4>CONTACT US</h4>
    <div style="padding-left:20px;font-weight:700;line-height:24px">COLM VESTRY</div>
    <div class="contact-row"><svg width="12" height="16" viewBox="0 0 12 16" style="margin-top:8px"><path d="M6 0a6 6 0 0 1 6 6c0 4-6 10-6 10S0 10 0 6a6 6 0 0 1 6-6z" fill="#1c1ccf"/><circle cx="6" cy="6" r="2" fill="#777"/></svg><span>14 Fern Lane, Westbrook<br>Park, Northvale 4021</span></div>
    <div class="contact-row"><svg width="14" height="14" viewBox="0 0 14 14" style="margin-top:9px"><path d="M3 0l3 3-2 2a8 8 0 0 0 5 5l2-2 3 3-2 3C6 14 0 8 0 2z" fill="#1c1ccf"/></svg><span>TELEPHONE: +(01) 555 0199</span></div>
    <div class="contact-row"><svg width="14" height="12" viewBox="0 0 14 12" style="margin-top:10px"><rect x="1" y="1" width="12" height="10" fill="none" stroke="#1c1ccf" stroke-width="2"/><path d="M1 1l6 5 6-5" fill="none" stroke="#1c1ccf" stroke-width="2"/></svg><span>hello@colmvestry-example.com</span></div>
  </div>
  <div class="fcol" style="left:892px"><h4>LOCATION</h4></div>
  <div class="abs map" role="img" aria-label="Map of the studio location"></div>
  <div class="copyright">All Rights Reserved Copyright 2013-2014</div>
</footer>

</body>
</html>
```